Tarn Vine Collective needs a new business card design

Colour theme: Gold + Red preferred
Front side: Main logo with my details as below;
Back side: Theme of some wine glasses or bottles, maybe different color of log together
Tarn Vine Collective

Leo Park
박 성민 (this is Korean character) on the English typying board: qkr tjdals
Managing Director

Suite 7/5 Harlow Rd
South Perth WA 6151
Tel) +61(8) 6272 3058
Mob) +61(402) 617 239

leo.park@tarnvinecollective.com
tarnvine@tarnvinecollective.com
www.tarnvinecollective.com

Target Market(s)

Asian Market

Industry/Entity Type

Business

Contact Information for Business Card

Tarn Vine Collective

Leo Park
박 성민 (this is Korean character) English typying: qkr tjdals
Managing Director

Suite 7/5 Harlow Rd
South Perth WA 6151
Tel) +61(8) 6272 3058
Mob) +61(402) 617 239

Font styles to use
Serif
Decorative

Colors
ec1f27
f78f21
f04a50
faa54b
cadf82
abd036

Requirements
Must have
• Company Logo & wine theme
Nice to have
• Very simple & modern
Should not have
• No Red Color on the name of Leo Park or 박 성민
• No traditional looking. young and modern look preferred

```html
<!DOCTYPE html>
<html lang="en">
<head>
<meta charset="utf-8">
<title>Tarn Vine Collective – Business Card</title>
<link rel="stylesheet" href="https://fonts.googleapis.com/css2?family=Questrial&family=Encode+Sans+Condensed:wght@400;500&family=Noto+Sans+KR:wght@400&display=swap">
<style>
  :root {
    --backdrop: #ece8e4;
    --card-white: #ffffff;
    --brand-red: #e23a2e;
    --deep-red: #b4231d;
    --bright-red: #d9352a;
    --gold: #c49a2c;
    --ink: #3a3a3a;
    --muted: #6b6b6b;
  }
  * { box-sizing: border-box; margin: 0; padding: 0; }
  html, body { width: 1200px; height: 1200px; overflow: hidden; }
  body {
    background: var(--backdrop);
    font-family: "Encode Sans Condensed", "Arial Narrow", sans-serif;
    color: var(--ink);
  }
  .sheet {
    position: relative;
    width: 1200px;
    height: 1200px;
  }
  .card {
    position: absolute;
    left: 150px;
    width: 900px;
    height: 514px;
    box-shadow: 0 10px 30px rgba(0,0,0,0.18);
    overflow: hidden;
  }
  .card--back {
    top: 56px;
    background: radial-gradient(ellipse at 45% 40%, var(--bright-red) 0%, #c42c23 45%, var(--deep-red) 100%);
  }
  .card--front {
    top: 630px;
    background: var(--card-white);
  }
  .front__band {
    position: absolute;
    left: 0; right: 0; bottom: 0;
    height: 44px;
    background: var(--brand-red);
  }
  .icon {
    display: block;
    width: 40px;
    height: 40px;
  }
  /* brand lockup */
  .brand {
    position: absolute;
    left: 70px;
    top: 150px;
    display: flex;
    align-items: center;
    gap: 18px;
  }
  .brand__dot {
    width: 64px; height: 64px;
    border-radius: 50%;
    background: var(--brand-red);
    flex: none;
  }
  .brand__name {
    font-family: "Encode Sans Condensed", "Arial Narrow", sans-serif;
    font-weight: 500;
    font-size: 40px;
    line-height: 1;
    color: var(--gold);
    letter-spacing: 0.5px;
  }
  .brand__tagline {
    margin-top: 8px;
    font-size: 17px;
    color: var(--gold);
  }
  .brand__url {
    font-size: 17px;
    color: var(--gold);
  }
  /* identity */
  .identity {
    position: absolute;
    left: 560px;
    top: 46px;
  }
  .identity__name {
    margin-top: 10px;
    font-family: "Questrial", sans-serif;
    font-size: 40px;
    letter-spacing: 1px;
    color: var(--gold);
    line-height: 1;
  }
  .identity__korean {
    margin-top: 8px;
    font-size: 18px;
    color: var(--muted);
  }
  .identity__korean .hangul { font-family: "Noto Sans KR", sans-serif; }
  .identity__role {
    font-size: 19px;
    color: var(--ink);
  }
  /* address */
  .address {
    position: absolute;
    right: 70px;
    top: 250px;
    text-align: left;
    font-size: 22px;
    line-height: 1.25;
  }
  .address .icon { margin-bottom: 10px; }
  /* phone */
  .phone {
    position: absolute;
    left: 70px;
    top: 330px;
    font-size: 24px;
    line-height: 1.25;
  }
  .phone .icon { margin-bottom: 10px; }
  .phone__label { color: var(--brand-red); }
  /* email */
  .email {
    position: absolute;
    left: 360px;
    top: 330px;
    font-size: 22px;
    line-height: 1.3;
  }
  .email .icon { margin-bottom: 10px; }
</style>
</head>
<body>
<main class="sheet">

  <section class="card card--back" aria-label="Card back: plain red field"></section>

  <section class="card card--front" aria-label="Card front">

    <div class="brand">
      <span class="brand__dot"></span>
      <div class="brand__text">
        <div class="brand__name">Tarn Vine Collective</div>
        <div class="brand__tagline">Connect &amp; Develop Your Business</div>
        <div class="brand__url">www.tarnvinecollective.com</div>
      </div>
    </div>

    <div class="identity">
      <svg class="icon" viewBox="0 0 40 40" aria-hidden="true">
        <circle cx="20" cy="20" r="20" fill="var(--brand-red)"/>
        <circle cx="20" cy="15" r="5.5" fill="var(--gold)"/>
        <path d="M10 29c1.5-6 5-8 10-8s8.5 2 10 8z" fill="var(--gold)"/>
      </svg>
      <div class="identity__name">LEO PARK</div>
      <div class="identity__korean"><span class="hangul">박 성민</span> - qkr tjdals</div>
      <div class="identity__role">Managing Director</div>
    </div>

    <div class="address">
      <svg class="icon" viewBox="0 0 40 40" aria-hidden="true">
        <circle cx="20" cy="20" r="20" fill="var(--brand-red)"/>
        <path d="M20 9a7 7 0 0 0-7 7c0 5.5 7 14 7 14s7-8.5 7-14a7 7 0 0 0-7-7z" fill="var(--gold)"/>
        <circle cx="20" cy="16" r="2.6" fill="var(--brand-red)"/>
      </svg>
      <div>Suite 7/5 Harlow Rd</div>
      <div>South Perth WA 6151</div>
    </div>

    <div class="phone">
      <svg class="icon" viewBox="0 0 40 40" aria-hidden="true">
        <circle cx="20" cy="20" r="20" fill="var(--brand-red)"/>
        <path d="M10 17c0-4 4-6 10-6s10 2 10 6l-4 1-1-3c-3-1-7-1-10 0l-1 3z" fill="var(--gold)"/>
        <path d="M13 20h14l2 9H11z" fill="var(--gold)"/>
        <circle cx="20" cy="24" r="2.5" fill="var(--brand-red)"/>
      </svg>
      <div><span class="phone__label">T :</span> +61(8) 6272 3058</div>
      <div><span class="phone__label">M :</span> +61(402) 617 239</div>
    </div>

    <div class="email">
      <svg class="icon" viewBox="0 0 40 40" aria-hidden="true">
        <circle cx="20" cy="20" r="20" fill="var(--brand-red)"/>
        <rect x="10" y="13" width="20" height="14" fill="var(--gold)"/>
        <path d="M10 13l10 8 10-8" fill="none" stroke="var(--brand-red)" stroke-width="1.6"/>
      </svg>
      <div>tarnvine@tarnvinecollective.com</div>
      <div>leo.park@tarnvinecollective.com</div>
    </div>

    <div class="front__band"></div>
  </section>

</main>
</body>
</html>
```